Horticulture Business Card Design Project

New garden service venture, I'd like design to reflect business name, Stillwood Yard Care garden services. Needs to be professional non comical and include a pic. I'd like to see designs in browns and greens as it will be printed on recycled paper to promote sustainability. I'd prefer a modern professonal card that is simple and catchy.
Updates

Thank u to all that submitted design/s -I really appreciated all of them.

Target Market(s)

Professional people aged between 40-60, that own their own homes and enjoy their gardens. Wanting a premium service that can be recommended to others by handing out the card and conveying a professional card that is impressive to potential clients.

Industry/Entity Type

Business

Requirements
Must have
• Picture relating to horticulture. One sided and including business name- Stillwood Yard Care Garden Services, Qualified Horticulturist, name, mobile number and email. Website is not needed. Id like a large green leaf pic such as monstera, ficus lyrata or rhaphis palms etc. Im open to ideas and welcome new suggestions. Simple fonts please
Nice to have
• Large green leaf as pic. Possibly like monstera or similar in size and impact. A modern touch
Should not have
• Comical pic

```html
<!DOCTYPE html>
<html lang="en">
<head>
<meta charset="utf-8">
<title>Stillwood Yard Care – Business Card</title>
<link rel="stylesheet" href="https://fonts.googleapis.com/css2?family=Questrial&display=swap">
<style>
  :root {
    --paper: #ffffff;
    --ink: #111111;
    --muted-ink: #555555;
    --night: #000000;
    --brand-green: #4fae3b;
    --leaf-deep: #1f4f14;
    --leaf-dark: #2f6b1f;
    --leaf-mid: #5f9e3a;
    --leaf-light: #a6d46f;
    --text-light: #ffffff;
    --text-soft: #cfcfcf;
  }
  * { box-sizing: border-box; margin: 0; padding: 0; }
  html, body {
    width: 987px;
    height: 1200px;
    overflow: hidden;
    background: var(--paper);
  }
  .card {
    position: relative;
    width: 987px;
    height: 1200px;
    font-family: "Questrial", "Century Gothic", sans-serif;
    background: var(--paper);
  }
  .card__header {
    position: absolute;
    left: 0; top: 0;
    width: 987px;
    height: 600px;
    background: var(--paper);
  }
  .brand-name {
    position: absolute;
    left: 0; right: 0;
    top: 232px;
    text-align: center;
    font-size: 100px;
    line-height: 1.1;
    font-weight: 400;
    letter-spacing: -1px;
    color: var(--brand-green);
    white-space: nowrap;
  }
  .brand-tagline {
    position: absolute;
    left: 0; right: 0;
    top: 362px;
    text-align: center;
    font-size: 36px;
    letter-spacing: 4px;
    color: var(--muted-ink);
    white-space: nowrap;
  }
  .website {
    position: absolute;
    left: 0; right: 0;
    top: 530px;
    text-align: center;
    font-size: 37px;
    color: var(--ink);
  }
  .card__contact {
    position: absolute;
    left: 0; top: 600px;
    width: 700px;
    height: 600px;
    background: var(--night);
    color: var(--text-light);
    text-align: center;
  }
  .contact__name {
    position: absolute;
    left: 0; right: 0;
    top: 120px;
    font-size: 54px;
    font-weight: 400;
    color: var(--brand-green);
  }
  .contact__role {
    position: absolute;
    left: 0; right: 0;
    top: 196px;
    font-size: 30px;
    color: var(--text-soft);
  }
  .contact__line {
    position: absolute;
    left: 0; right: 0;
    font-size: 38px;
    white-space: nowrap;
  }
  .contact__address { top: 275px; }
  .contact__phone   { top: 345px; }
  .contact__email   { top: 415px; font-size: 34px; }
  .card__divider {
    position: absolute;
    left: 700px; top: 600px;
    width: 6px; height: 600px;
    background: var(--paper);
  }
  .leaf-photo {
    position: absolute;
    left: 706px; top: 600px;
    width: 281px; height: 600px;
    background:
      radial-gradient(ellipse 70% 45% at 35% 60%, var(--leaf-light) 0%, rgba(166,212,111,0) 70%),
      linear-gradient(160deg, var(--leaf-dark) 0%, var(--leaf-mid) 45%, var(--leaf-dark) 80%, var(--leaf-deep) 100%);
  }
</style>
</head>
<body>
  <main class="card">
    <section class="card__header">
      <h1 class="brand-name">Stillwood Yard Care</h1>
      <p class="brand-tagline">GARDEN SERVICES</p>
      <p class="website">www.stillwoodyardcare.com</p>
    </section>

    <section class="card__contact">
      <h2 class="contact__name">Dana Whitlock</h2>
      <p class="contact__role">Qualified Horticulturist</p>
      <p class="contact__line contact__address">48 Fernhill Road Brookvale 2100</p>
      <p class="contact__line contact__phone">0400 555 019</p>
      <p class="contact__line contact__email">dwhitlock@stillwoodyardcare.com</p>
    </section>

    <div class="card__divider"></div>
    <div class="leaf-photo" role="img" aria-label="Close-up photograph of a large green monstera leaf with water droplets"></div>
  </main>
</body>
</html>
```